MTSS Pyramid graphic needed for use in presentations and on my website

I am a consultant and need graphics to represent the MTSS pyramid (educational terminology) for use on my website and in slide decks. I've included documentation below that shows the MTSS pyramid, some preferences I have thought of, and my color palette. The MTSS pyramid is well-known in my field and I'd like one that I can use in all my presentations and on my website that looks professional and modern.

Target Market(s)

Educational leaders and educators

Industry/Entity Type

Educational Consulting

Font styles to use
Serif
Sans Serif

Colors
00AB8E
00BBA5
67D7C9
C6EFE9
E9F9F6
6B429C
8869AF
B7A5CE
E3DAEB
F3F0F8

Requirements
Must have
• a pyramid that can be recognized as an MTSS pyramid, use of colors that align with my color palette, a professional, modern look and feel, 3 sections with the largest at the bottom of the pyramid
Nice to have
• rounded corners, maybe 3D
Should not have
• a pyramid in a different shape or orientation, any more or fewer than 3 sections

```html
<!DOCTYPE html>
<html lang="en">
<head>
<meta charset="utf-8">
<title>MTSS Pyramid Set</title>
<link href="https://fonts.googleapis.com/css2?family=Roboto:wght@700&display=swap" rel="stylesheet">
<style>
  :root {
    --bg: #ffffff;
    --purple-light: #8869af;
    --purple-dark: #6b429c;
    --lavender-light: #b7a5ce;
    --lavender-dark: #8869af;
    --teal-light: #67d7c9;
    --teal-dark: #00ab8e;
    --gray-light: #e3e3e3;
    --gray-dark: #c7c7c7;
    --divider: #f4f4f4;
    --label-on-color: #ffffff;
    --label-on-gray: #7b7b7b;
  }
  html, body {
    margin: 0;
    padding: 0;
    width: 1200px;
    height: 2573px;
    overflow: hidden;
    background: var(--bg);
  }
  .canvas {
    position: relative;
    width: 1200px;
    height: 2573px;
  }
  .defs { position: absolute; width: 0; height: 0; }
  .pyramid {
    position: absolute;
    width: 421px;
    height: 424px;
    overflow: visible;
  }
  .col-labeled { left: 163px; }
  .col-plain { left: 647px; }
  .row-1 { top: 84px; }
  .row-2 { top: 566px; }
  .row-3 { top: 1052px; }
  .row-4 { top: 1537px; }
  .row-5 { top: 2022px; }

  .stop-purple-l { stop-color: var(--purple-light); }
  .stop-purple-d { stop-color: var(--purple-dark); }
  .stop-lavender-l { stop-color: var(--lavender-light); }
  .stop-lavender-d { stop-color: var(--lavender-dark); }
  .stop-teal-l { stop-color: var(--teal-light); }
  .stop-teal-d { stop-color: var(--teal-dark); }
  .stop-gray-l { stop-color: var(--gray-light); }
  .stop-gray-d { stop-color: var(--gray-dark); }

  .fill-purple { fill: url(#grad-purple); }
  .fill-lavender { fill: url(#grad-lavender); }
  .fill-teal { fill: url(#grad-teal); }
  .fill-gray { fill: url(#grad-gray); }

  .tier-divider { stroke: var(--divider); stroke-width: 2.2; opacity: 0.9; }
  .pyramid-edge { fill: none; stroke: rgba(0,0,0,0.12); stroke-width: 3; }

  .tier-label {
    font-family: 'Roboto', sans-serif;
    font-weight: 700;
    text-anchor: middle;
    dominant-baseline: central;
  }
  .label-top { font-size: 15px; }
  .label-mid { font-size: 18px; }
  .label-base { font-size: 20px; }
  .on-color { fill: var(--label-on-color); }
  .on-gray { fill: var(--label-on-gray); }
</style>
</head>
<body>
<main class="canvas">

  <svg class="defs" aria-hidden="true">
    <defs>
      <clipPath id="pyramid-shape">
        <path id="pyramid-outline" d="M123.7,20 A35,35 0 0 1 187.3,20 L305,258 Q318,282 303,300 Q291,313 273,313 L38,313 Q20,313 8,300 Q-6,282 6,258 Z"/>
      </clipPath>
      <radialGradient id="grad-purple" cx="0.5" cy="0.5" r="0.6">
        <stop offset="0" class="stop-purple-l"/><stop offset="1" class="stop-purple-d"/>
      </radialGradient>
      <radialGradient id="grad-lavender" cx="0.5" cy="0.5" r="0.55">
        <stop offset="0" class="stop-lavender-l"/><stop offset="1" class="stop-lavender-d"/>
      </radialGradient>
      <radialGradient id="grad-teal" cx="0.5" cy="0.5" r="0.55">
        <stop offset="0" class="stop-teal-l"/><stop offset="1" class="stop-teal-d"/>
      </radialGradient>
      <radialGradient id="grad-gray" cx="0.5" cy="0.5" r="0.55">
        <stop offset="0" class="stop-gray-l"/><stop offset="1" class="stop-gray-d"/>
      </radialGradient>
    </defs>
  </svg>

  <!-- Row 1: all tiers -->
  <svg class="pyramid col-labeled row-1" viewBox="0 0 312 314" role="img" aria-label="MTSS pyramid, all three tiers highlighted">
    <g clip-path="url(#pyramid-shape)">
      <rect class="fill-purple" x="0" y="0" width="312" height="78"/>
      <rect class="fill-lavender" x="0" y="78" width="312" height="103"/>
      <rect class="fill-teal" x="0" y="181" width="312" height="133"/>
      <line class="tier-divider" x1="0" y1="78" x2="312" y2="78"/>
      <line class="tier-divider" x1="0" y1="181" x2="312" y2="181"/>
    </g>
    <use href="#pyramid-outline" class="pyramid-edge"/>
    <text class="tier-label label-top on-color" x="156" y="44">Tier 3</text>
    <text class="tier-label label-mid on-color" x="156" y="133">Tier 2</text>
    <text class="tier-label label-base on-color" x="156" y="249">Tier 1</text>
  </svg>
  <svg class="pyramid col-plain row-1" viewBox="0 0 312 314" role="img" aria-label="MTSS pyramid, all three tiers highlighted, unlabeled">
    <g clip-path="url(#pyramid-shape)">
      <rect class="fill-purple" x="0" y="0" width="312" height="78"/>
      <rect class="fill-lavender" x="0" y="78" width="312" height="103"/>
      <rect class="fill-teal" x="0" y="181" width="312" height="133"/>
      <line class="tier-divider" x1="0" y1="78" x2="312" y2="78"/>
      <line class="tier-divider" x1="0" y1="181" x2="312" y2="181"/>
    </g>
    <use href="#pyramid-outline" class="pyramid-edge"/>
  </svg>

  <!-- Row 2: tier 1 -->
  <svg class="pyramid col-labeled row-2" viewBox="0 0 312 314" role="img" aria-label="MTSS pyramid, tier 1 highlighted">
    <g clip-path="url(#pyramid-shape)">
      <rect class="fill-gray" x="0" y="0" width="312" height="78"/>
      <rect class="fill-gray" x="0" y="78" width="312" height="103"/>
      <rect class="fill-teal" x="0" y="181" width="312" height="133"/>
      <line class="tier-divider" x1="0" y1="78" x2="312" y2="78"/>
      <line class="tier-divider" x1="0" y1="181" x2="312" y2="181"/>
    </g>
    <use href="#pyramid-outline" class="pyramid-edge"/>
    <text class="tier-label label-top on-gray" x="156" y="44">Tier 3</text>
    <text class="tier-label label-mid on-gray" x="156" y="133">Tier 2</text>
    <text class="tier-label label-base on-color" x="156" y="249">Tier 1</text>
  </svg>
  <svg class="pyramid col-plain row-2" viewBox="0 0 312 314" role="img" aria-label="MTSS pyramid, tier 1 highlighted, unlabeled">
    <g clip-path="url(#pyramid-shape)">
      <rect class="fill-gray" x="0" y="0" width="312" height="78"/>
      <rect class="fill-gray" x="0" y="78" width="312" height="103"/>
      <rect class="fill-teal" x="0" y="181" width="312" height="133"/>
      <line class="tier-divider" x1="0" y1="78" x2="312" y2="78"/>
      <line class="tier-divider" x1="0" y1="181" x2="312" y2="181"/>
    </g>
    <use href="#pyramid-outline" class="pyramid-edge"/>
  </svg>

  <!-- Row 3: tier 2 -->
  <svg class="pyramid col-labeled row-3" viewBox="0 0 312 314" role="img" aria-label="MTSS pyramid, tier 2 highlighted">
    <g clip-path="url(#pyramid-shape)">
      <rect class="fill-gray" x="0" y="0" width="312" height="78"/>
      <rect class="fill-lavender" x="0" y="78" width="312" height="103"/>
      <rect class="fill-gray" x="0" y="181" width="312" height="133"/>
      <line class="tier-divider" x1="0" y1="78" x2="312" y2="78"/>
      <line class="tier-divider" x1="0" y1="181" x2="312" y2="181"/>
    </g>
    <use href="#pyramid-outline" class="pyramid-edge"/>
    <text class="tier-label label-top on-gray" x="156" y="44">Tier 3</text>
    <text class="tier-label label-mid on-color" x="156" y="133">Tier 2</text>
    <text class="tier-label label-base on-gray" x="156" y="249">Tier 1</text>
  </svg>
  <svg class="pyramid col-plain row-3" viewBox="0 0 312 314" role="img" aria-label="MTSS pyramid, tier 2 highlighted, unlabeled">
    <g clip-path="url(#pyramid-shape)">
      <rect class="fill-gray" x="0" y="0" width="312" height="78"/>
      <rect class="fill-lavender" x="0" y="78" width="312" height="103"/>
      <rect class="fill-gray" x="0" y="181" width="312" height="133"/>
      <line class="tier-divider" x1="0" y1="78" x2="312" y2="78"/>
      <line class="tier-divider" x1="0" y1="181" x2="312" y2="181"/>
    </g>
    <use href="#pyramid-outline" class="pyramid-edge"/>
  </svg>

  <!-- Row 4: tier 3 -->
  <svg class="pyramid col-labeled row-4" viewBox="0 0 312 314" role="img" aria-label="MTSS pyramid, tier 3 highlighted">
    <g clip-path="url(#pyramid-shape)">
      <rect class="fill-purple" x="0" y="0" width="312" height="78"/>
      <rect class="fill-gray" x="0" y="78" width="312" height="103"/>
      <rect class="fill-gray" x="0" y="181" width="312" height="133"/>
      <line class="tier-divider" x1="0" y1="78" x2="312" y2="78"/>
      <line class="tier-divider" x1="0" y1="181" x2="312" y2="181"/>
    </g>
    <use href="#pyramid-outline" class="pyramid-edge"/>
    <text class="tier-label label-top on-color" x="156" y="44">Tier 3</text>
    <text class="tier-label label-mid on-gray" x="156" y="133">Tier 2</text>
    <text class="tier-label label-base on-gray" x="156" y="249">Tier 1</text>
  </svg>
  <svg class="pyramid col-plain row-4" viewBox="0 0 312 314" role="img" aria-label="MTSS pyramid, tier 3 highlighted, unlabeled">
    <g clip-path="url(#pyramid-shape)">
      <rect class="fill-purple" x="0" y="0" width="312" height="78"/>
      <rect class="fill-gray" x="0" y="78" width="312" height="103"/>
      <rect class="fill-gray" x="0" y="181" width="312" height="133"/>
      <line class="tier-divider" x1="0" y1="78" x2="312" y2="78"/>
      <line class="tier-divider" x1="0" y1="181" x2="312" y2="181"/>
    </g>
    <use href="#pyramid-outline" class="pyramid-edge"/>
  </svg>

  <!-- Row 5: tiers 1 and 2 -->
  <svg class="pyramid col-labeled row-5" viewBox="0 0 312 314" role="img" aria-label="MTSS pyramid, tiers 1 and 2 highlighted">
    <g clip-path="url(#pyramid-shape)">
      <rect class="fill-gray" x="0" y="0" width="312" height="78"/>
      <rect class="fill-lavender" x="0" y="78" width="312" height="103"/>
      <rect class="fill-teal" x="0" y="181" width="312" height="133"/>
      <line class="tier-divider" x1="0" y1="78" x2="312" y2="78"/>
      <line class="tier-divider" x1="0" y1="181" x2="312" y2="181"/>
    </g>
    <use href="#pyramid-outline" class="pyramid-edge"/>
    <text class="tier-label label-top on-gray" x="156" y="44">Tier 3</text>
    <text class="tier-label label-mid on-color" x="156" y="133">Tier 2</text>
    <text class="tier-label label-base on-color" x="156" y="249">Tier 1</text>
  </svg>
  <svg class="pyramid col-plain row-5" viewBox="0 0 312 314" role="img" aria-label="MTSS pyramid, tiers 1 and 2 highlighted, unlabeled">
    <g clip-path="url(#pyramid-shape)">
      <rect class="fill-gray" x="0" y="0" width="312" height="78"/>
      <rect class="fill-lavender" x="0" y="78" width="312" height="103"/>
      <rect class="fill-teal" x="0" y="181" width="312" height="133"/>
      <line class="tier-divider" x1="0" y1="78" x2="312" y2="78"/>
      <line class="tier-divider" x1="0" y1="181" x2="312" y2="181"/>
    </g>
    <use href="#pyramid-outline" class="pyramid-edge"/>
  </svg>

</main>
</body>
</html>
```